promotional flyer for Valtera Gym

we are after a double sided a5 leaflet to promote our gym, this is to go out to the general public to entice them into getting membership.

gym membership is £30 per month

it should also include the offer of - if you present this leaflet then there will be no joining fee

some of the features of the gym include

strength machines
cardio machines
functional area
sprung floor mat area

Target Market(s)

Adults 16+ who want to go to the gym and workout

Industry/Entity Type

Gym

Font styles to use
Other font styles liked:
• montserrat Regular

Requirements
Must have
• Clean on brand design
• use images supplied by us
Nice to have
• focus on an inclusive experience as the gym will be advertised to everyone
• should also use our "fitter, stronger, Healthier"

```html
<!DOCTYPE html>
<html lang="en">
<head>
<meta charset="utf-8">
<title>Valtera Gym – Membership Flyer</title>
<link rel="stylesheet" href="https://fonts.googleapis.com/css2?family=Montserrat:wght@500;600;800&family=Roboto+Condensed:wght@700&display=swap">
<style>
  :root {
    --orange: #f5411e;
    --orange-deep: #e0301a;
    --silver-dark: #8e8e8e;
    --silver-mid: #c4c4c4;
    --silver-light: #f4f4f4;
    --white: #ffffff;
    --photo-dark: #4a3d3a;
    --photo-mid: #8a6d5c;
  }
  * { margin: 0; padding: 0; box-sizing: border-box; }
  html, body { width: 902px; height: 1200px; overflow: hidden; background: var(--white); }
  .flyer {
    position: absolute; left: 83px; top: 74px; width: 732px; height: 1048px; overflow: hidden;
    background: linear-gradient(90deg, var(--silver-dark) 0%, var(--silver-light) 22%, var(--silver-mid) 45%, var(--silver-dark) 70%, var(--silver-light) 100%);
    font-family: "Montserrat", sans-serif;
  }
  .shapes { position: absolute; inset: 0; }
  .photo { position: absolute; }
  .photo--spin {
    left: 380px; top: 30px; width: 352px; height: 366px;
    clip-path: polygon(30px 0, 100% 0, 100% 100%, 0 100%);
    background: linear-gradient(160deg, var(--photo-dark) 0%, #6b5a55 40%, var(--photo-mid) 75%, #b39a84 100%);
  }
  .photo--strength {
    left: 292px; top: 414px; width: 394px; height: 398px;
    background: linear-gradient(150deg, #2f3f66 0%, #5a5060 40%, var(--photo-mid) 75%, #cfc8c2 100%);
  }
  .headline {
    position: absolute; left: 0; top: 34px; width: 348px; text-align: center;
    color: var(--orange); font-weight: 800; font-size: 44px; line-height: 100px;
    -webkit-text-stroke: 6px var(--white); paint-order: stroke fill;
    text-shadow: 0 3px 6px rgba(0,0,0,.35);
  }
  .price-band {
    position: absolute; left: 0; top: 400px; width: 324px; height: 84px;
    background: var(--orange); color: var(--white);
    display: flex; align-items: center; justify-content: center; text-align: center;
    font-weight: 500; font-size: 21px; line-height: 1.4;
  }
  .features { position: absolute; left: 33px; top: 580px; list-style: none; }
  .features li {
    font-family: "Roboto Condensed", sans-serif; font-weight: 700; font-size: 21px; line-height: 30px;
    color: var(--orange); text-transform: uppercase; transform: rotate(2deg); transform-origin: left center;
    text-shadow: 0 2px 3px rgba(0,0,0,.3); height: 82px;
  }
  .brand-dot {
    position: absolute; left: 438px; top: 847px; width: 112px; height: 112px;
    border-radius: 50%; background: var(--orange);
  }
  .brand-name {
    position: absolute; left: 274px; top: 968px; width: 440px; text-align: center;
    color: var(--white); font-weight: 600; font-size: 38px; line-height: 46px; letter-spacing: 4px; text-transform: uppercase;
  }
</style>
</head>
<body>
<main class="flyer">
  <svg class="shapes" width="732" height="1048" viewBox="0 0 732 1048">
    <polygon points="628,0 732,0 732,92" fill="var(--white)"/>
    <polygon points="378,0 412,0 362,400 324,400" fill="var(--orange)"/>
    <polygon points="324,484 352,484 300,820 278,820" fill="var(--orange-deep)"/>
    <polygon points="732,600 732,660 640,1048 600,1048" fill="var(--orange)"/>
    <polygon points="732,700 732,740 680,1048 660,1048" fill="var(--orange)"/>
    <polygon points="715,520 732,500 732,540 700,640" fill="var(--white)"/>
    <rect x="0" y="992" width="235" height="56" fill="var(--orange)"/>
  </svg>

  <div class="photo photo--spin" role="img" aria-label="Photo of two women riding spin bikes in the gym studio"></div>
  <div class="photo photo--strength" role="img" aria-label="Photo of a woman training on a strength machine"></div>

  <h1 class="headline">FITTER<br>STRONGER<br>HEALTHIER</h1>

  <p class="price-band">GYM MEMBERSHIP IS<br>£30 PER MONTH</p>

  <ul class="features">
    <li>Sprung floor mat area</li>
    <li>Strength machines</li>
    <li>Cardio machines</li>
    <li>Functional area</li>
  </ul>

  <span class="brand-dot"></span>
  <p class="brand-name">Valtera Gym</p>
</main>
</body>
</html>
```